Birthday Card for Employees*

I'd like a birthday card designed using company logo to be given to employees

Colors

Designer to choose colors to be used in the design.

Requirements
Must have
• KRV Logos

```html
<!DOCTYPE html>
<html lang="en">
<head>
<meta charset="utf-8">
<title>KRV Solutions – Employee Birthday Card</title>
<link href="https://fonts.googleapis.com/css2?family=Lato:wght@400;700&family=Arimo:wght@400;700&family=Montserrat:wght@500;700&display=swap" rel="stylesheet">
<style>
  :root {
    --paper: #ffffff;
    --paper-edge: #ececef;
    --brand-blue: #3b86cc;
    --navy: #323a52;
    --logo-grey: #8d929c;
    --tagline: #4a5a74;
    --message: #ffffff;
  }
  html, body {
    margin: 0;
    padding: 0;
    width: 1200px;
    height: 1000px;
    overflow: hidden;
    background: var(--paper);
  }
  .canvas {
    position: relative;
    width: 1200px;
    height: 1000px;
  }

  /* Inside spread */
  .card-inside {
    position: absolute;
    left: 553px;
    top: 118px;
    width: 520px;
    height: 730px;
    background: var(--paper);
    border: 2px solid var(--paper-edge);
    box-sizing: border-box;
    z-index: 1;
  }
  .tagline {
    position: absolute;
    left: 38px;
    top: 30px;
    margin: 0;
    font-family: "Montserrat", sans-serif;
    font-weight: 500;
    font-size: 15px;
    line-height: 19px;
    color: var(--tagline);
    list-style: none;
    padding: 0;
  }
  .tagline b {
    font-weight: 700;
    color: var(--brand-blue);
  }
  .inside-panel {
    position: absolute;
    left: -2px;
    right: -2px;
    bottom: -2px;
    height: 366px;
    background: var(--navy);
  }
  .birthday-message {
    position: absolute;
    left: 0;
    right: 0;
    top: 112px;
    margin: 0;
    text-align: center;
    font-family: "Arimo", sans-serif;
    font-size: 17px;
    line-height: 21.5px;
    color: var(--message);
  }
  .birthday-message strong { font-weight: 700; }

  /* Wordmark stand-in */
  .wordmark {
    display: flex;
    align-items: center;
    gap: 8px;
    font-family: "Lato", sans-serif;
    font-weight: 700;
    font-size: 17px;
    letter-spacing: 1.5px;
    color: var(--logo-grey);
    white-space: nowrap;
  }
  .wordmark-square {
    width: 12px;
    height: 12px;
    background: var(--logo-grey);
  }
  .inside-panel .wordmark {
    position: absolute;
    left: 0;
    right: 0;
    top: 316px;
    justify-content: center;
  }

  /* Front cover */
  .card-front {
    position: absolute;
    left: 128px;
    top: 230px;
    width: 520px;
    height: 366px;
    background: var(--paper);
    border: 2px solid var(--paper-edge);
    box-sizing: border-box;
    z-index: 2;
  }
  .front-frame {
    position: absolute;
    left: 50px;
    top: 35px;
    width: 418px;
    height: 293px;
    border: 6px solid var(--brand-blue);
    box-sizing: border-box;
  }
  .front-title {
    position: absolute;
    left: 0;
    right: 0;
    top: 104px;
    margin: 0;
    text-align: center;
    font-family: "Lato", sans-serif;
    font-weight: 400;
    font-size: 63px;
    line-height: 74px;
    letter-spacing: 0.5px;
    color: var(--brand-blue);
  }
  .front-tab {
    position: absolute;
    left: 117px;
    top: 289px;
    width: 282px;
    height: 75px;
    background: var(--navy);
    display: flex;
    align-items: center;
    justify-content: center;
  }
</style>
</head>
<body>
<main class="canvas">

  <section class="card-inside" aria-label="Card inside">
    <ul class="tagline">
      <li><b>K</b>nowledge.</li>
      <li><b>R</b>eliability.</li>
      <li><b>V</b>ision.</li>
      <li><b>S</b>afety</li>
    </ul>
    <div class="inside-panel">
      <p class="birthday-message">
        We wish your birthday<br>
        will be defined by love, joy and happiness.<br>
        We hope that you will be graced with the strength<br>
        to accomplish all that you aspire<br>
        in your days ahead.<br>
        <strong>Happy birthday!</strong>
      </p>
      <div class="wordmark"><span class="wordmark-square"></span>KRV SOLUTIONS</div>
    </div>
  </section>

  <section class="card-front" aria-label="Card front cover">
    <div class="front-frame"></div>
    <h1 class="front-title">BIRTHDAY<br>WISHES</h1>
    <div class="front-tab">
      <div class="wordmark"><span class="wordmark-square"></span>KRV SOLUTIONS</div>
    </div>
  </section>

</main>
</body>
</html>
```